Letterhead to Introduce a 'Sister' Company.

What I am needing is a design for a letter head to introduce our current customers base of (KT Alarm) customers to our new service, 'Kestrel Tide Solar Brokers'

```html
<!DOCTYPE html>
<html lang="en">
<head>
<meta charset="utf-8">
<title>KT Alarm – Kestrel Tide Solar Brokers Letterhead</title>
<link href="https://fonts.googleapis.com/css2?family=Open+Sans:wght@400;700&family=Roboto:wght@400&display=swap" rel="stylesheet">
<style>
  :root {
    --backdrop: #dedede;
    --paper: #f8f8f8;
    --body-text: #5a5a5a;
    --footer-text: #3c3c3c;
    --alarm-green: #43ac3a;
    --solar-blue: #1d4a87;
    --solar-orange: #f29a1f;
    --signature-tint: #e9ebf0;
  }
  * { box-sizing: border-box; margin: 0; padding: 0; }
  html, body {
    width: 1153px; height: 1200px; overflow: hidden;
    background: var(--backdrop);
  }
  .letterhead {
    position: absolute; left: 161px; top: 20px;
    width: 831px; height: 1160px;
    background: var(--paper);
    box-shadow: 0 6px 24px rgba(0,0,0,0.12);
    font-family: "Open Sans", Arial, sans-serif;
  }
  .brand-alarm {
    position: absolute; left: 75px; top: 104px;
    font-size: 34px; font-weight: 700; letter-spacing: 1px;
    color: var(--alarm-green); line-height: 1;
  }
  .brand-solar {
    position: absolute; right: 74px; top: 84px;
    display: flex; align-items: center; gap: 12px;
  }
  .brand-solar .mark-dot {
    width: 34px; height: 34px; border-radius: 50%;
    background: var(--solar-orange);
  }
  .brand-solar .name {
    font-size: 20px; font-weight: 700; line-height: 1.15;
    color: var(--solar-blue); text-align: right;
  }
  .letter-body {
    position: absolute; left: 75px; top: 239px; width: 682px;
    font-size: 14.6px; line-height: 22.3px; color: var(--body-text);
  }
  .letter-body p { margin-bottom: 22.3px; text-align: justify; }
  .letter-body .greeting, .letter-body .closing { text-align: left; }
  .signature-area {
    position: absolute; left: 75px; top: 827px;
    width: 100px; height: 92px;
    background: var(--signature-tint); border-radius: 4px;
  }
  .contact-list {
    position: absolute; left: 75px; top: 1026px;
    list-style: none;
    font-family: "Roboto", Arial, sans-serif;
    font-size: 16.5px; line-height: 22.3px; color: var(--footer-text);
  }
  .contact-list li { display: flex; align-items: center; gap: 6px; }
  .contact-list svg { width: 15px; height: 15px; flex: none; }
  .postal-address {
    position: absolute; right: 74px; top: 1048px;
    font-family: "Roboto", Arial, sans-serif; font-style: normal;
    font-size: 16.5px; line-height: 22.3px; color: var(--footer-text);
    text-align: right;
  }
</style>
</head>
<body>
  <main class="letterhead">
    <header>
      <div class="brand-alarm">KT Alarm</div>
      <div class="brand-solar">
        <span class="mark-dot"></span>
        <div class="name">Kestrel Tide<br>Solar Brokers</div>
      </div>
    </header>

    <section class="letter-body">
      <p class="greeting">Dear customer,</p>
      <p>Lorem ipsum dolor sit amet, consectetur adipisicing elit, sed do eiusmod tempor incididunt ut labore et dolore magna aliqua. Ut enim ad minim veniam, quis nostrud exercitation ullamco laboris nisi ut aliquip ex ea commodo consequat. Duis aute irure dolor in reprehenderit in voluptate velit esse cillum dolore eu fugiat nulla pariatur. Excepteur sint occaecat cupidatat non proident, sunt in culpa qui officia deserunt mollit anim id est laborum.</p>
      <p>Lorem ipsum dolor sit amet, consectetur adipisicing elit, sed do eiusmod tempor incididunt ut labore et dolore magna aliqua. Ut enim ad minim veniam, quis nostrud exercitation ullamco laboris nisi ut aliquip ex ea commodo consequat. Duis aute irure dolor in reprehenderit in voluptate velit esse cillum dolore eu fugiat nulla pariatur. Excepteur sint occaecat cupidatat non proident, sunt in culpa qui officia deserunt mollit anim id est laborum.</p>
      <p>Lorem ipsum dolor sit amet, consectetur adipisicing elit, sed do eiusmod tempor incididunt ut labore et dolore magna aliqua. Ut enim ad minim veniam, quis nostrud exercitation ullamco laboris nisi ut aliquip ex ea commodo consequat. Duis aute irure dolor in reprehenderit in voluptate velit esse cillum dolore eu fugiat nulla pariatur. Excepteur sint occaecat cupidatat non proident, sunt in culpa qui officia deserunt mollit anim id est laborum.</p>
      <p>Lorem ipsum dolor sit amet, consectetur adipisicing elit, sed do eiusmod tempor incididunt ut labore et dolore magna aliqua. Ut enim ad minim veniam, quis nostrud exercitation ullamco laboris nisi ut aliquip ex ea commodo consequat. Duis aute irure dolor in reprehenderit.</p>
      <p class="closing">Yours Sincerely,</p>
    </section>

    <div class="signature-area" role="img" aria-label="Handwritten signature of the sender"></div>

    <footer>
      <ul class="contact-list">
        <li>
          <svg viewBox="0 0 16 16" aria-hidden="true"><path fill="var(--alarm-green)" d="M1 6c0-2 3-3 7-3s7 1 7 3v1.5h-3.5V6h-7v1.5H1zM4 8.5l1.5-2h5l1.5 2V13H4zM8 8.6a1.9 1.9 0 1 0 0 3.8a1.9 1.9 0 0 0 0-3.8z"/></svg>
          905.218.4470
        </li>
        <li>
          <svg viewBox="0 0 16 16" aria-hidden="true"><rect x="1" y="3" width="14" height="10" fill="var(--alarm-green)"/><path d="M1.5 3.5L8 9l6.5-5.5M1.5 12.5l4.5-4.5M14.5 12.5L10 8" stroke="#fff" stroke-width="1.1" fill="none"/></svg>
          info@KTAlarm.com
        </li>
        <li>
          <svg viewBox="0 0 16 16" aria-hidden="true"><circle cx="8" cy="8" r="7" fill="var(--alarm-green)"/><path d="M4 4.5c1.5 0 2 1 3 1.5s.5 2-.5 2.5S5 10.5 5 12M10 3.5c0 1.5 1 2 2 2.5M11 9.5c-1 .5-1.5 1.5-1 3" stroke="#fff" stroke-width="1.3" fill="none"/></svg>
          www.KTAlarm.com
        </li>
      </ul>
      <address class="postal-address">48 Harbour Crest Lane,<br>Millbrook Bay, ON L7K 3R2</address>
    </footer>
  </main>
</body>
</html>
```